design a company brochure

tri-fold brochure. reference website: orvanta.llc for information (website under construction but should have the basic information)

Target Market(s)

Users of sign Language interpreting services; businesses, community, hospitals, schools, colleges, medical, religious, and legal settings

Industry/Entity Type

Community Service

Font styles to use
Serif
Decorative

Colors
734ea0
9ccb3b

Requirements
Must have
• Brochure should be worded so it applies to the above markets and focuses on our professionalism, integrity in business
Nice to have
• I would like the designers to look at the business website under construction (orvanta.llc) or an older website (orvanta-tkpr.com). Company was restructured and is now just ORVANTA, LLC.
A darker green than what is shown here. Again, reference the website
Should not have
• No personal pictures in the brochure - can use clip art or interpreter/interpreting shots.

```html
<!DOCTYPE html>
<html lang="en">
<head>
<meta charset="utf-8">
<title>ORVANTA, LLC – Tri-fold Brochure</title>
<link rel="stylesheet" href="https://fonts.googleapis.com/css2?family=Roboto+Slab:wght@800;900&family=Signika:wght@600;700&family=Dosis:wght@500;600&family=Open+Sans:wght@400;600;700&display=swap">
<style>
:root{
  --bg:#3a3a3a;
  --plum:#4d1d3f;
  --plum-deep:#3e1533;
  --green:#6a8a31;
  --green-dark:#587528;
  --lime:#a7cc3c;
  --paper:#f4f4f3;
  --ink:#2b2b2b;
  --white:#ffffff;
  --photo-warm:#c9b6a3;
  --photo-green:#4f6a3a;
}
*{box-sizing:border-box;margin:0;padding:0}
html,body{width:1200px;height:3477px;overflow:hidden;background:var(--bg)}
body{position:relative;font-family:"Open Sans",sans-serif}
.spread{position:absolute;left:56px;width:1088px;height:840px;display:grid;grid-template-columns:repeat(3,1fr);box-shadow:0 10px 30px rgba(0,0,0,.45)}
.spread--outside{top:876px}
.spread--inside{top:1764px}
.panel{position:relative;overflow:hidden}
.abs{position:absolute}
.heading{font-family:"Signika",sans-serif;font-weight:700;text-transform:uppercase;letter-spacing:.5px}
.placeholder{position:absolute}

/* About panel */
.about{background:var(--plum)}
.about .heading{left:0;right:0;top:26px;text-align:center;color:var(--white);font-size:29px;z-index:2}
.portrait{width:126px;height:126px;border-radius:50%;border:5px solid var(--white);background:radial-gradient(circle at 50% 40%,#9d8273,#4a3a34)}
.person{width:150px;text-align:center;color:var(--white);font-size:11px;line-height:14px}
.person b{display:block;font-weight:700;text-transform:uppercase}
.about-copy{left:36px;right:36px;top:312px;color:var(--white);font-size:10.4px;line-height:13.4px;text-align:justify}
.about-copy p+p{margin-top:10px}

/* Careers panel */
.careers{background:var(--green);color:var(--white);text-align:center}
.map{left:60px;top:56px;width:243px;height:243px;border-radius:50%;border:6px solid #d8d8d8;background:linear-gradient(135deg,#e8e6df,#cfd3cc)}
.careers .heading{left:0;right:0;font-size:28px}
.careers-copy{left:34px;right:34px;top:360px;font-family:"Signika",sans-serif;font-weight:600;font-size:14.5px;line-height:20px}
.contact{left:0;right:0;top:566px;font-family:"Dosis",sans-serif;font-weight:500;font-size:17px;line-height:21.6px}
.contact b{font-weight:600}
.request{left:34px;width:294px;height:90px;border:2px solid var(--white);border-radius:4px;display:flex;align-items:center;gap:14px;padding-left:20px;text-align:left}
.request-label{font-family:"Signika",sans-serif;font-weight:700;font-size:28px;line-height:28px;text-transform:uppercase;color:var(--white)}

/* Cover panel */
.cover{background:var(--paper)}
.cover-top{left:0;right:0;top:0;height:560px;background:linear-gradient(180deg,#e4dbe8 0%,#ecefdd 45%,#f2efe6 100%)}
.brand{left:54px;top:66px;display:flex;align-items:center;gap:12px}
.brand-mark{width:52px;height:52px;border:4px solid var(--ink)}
.brand-name{font-family:"Signika",sans-serif;font-weight:700;font-size:20px;color:var(--ink)}
.title{left:0;right:0;top:620px;text-align:center;font-family:"Roboto Slab",serif;font-weight:900;font-size:46px;line-height:48px;color:var(--plum)}
.subtitle{left:0;right:0;top:746px;text-align:center;font-family:"Dosis",sans-serif;font-weight:600;font-size:18px;color:var(--ink);letter-spacing:.5px}
.url-tab{left:64px;width:234px;bottom:0;height:48px;background:var(--plum);border-radius:16px 16px 0 0;color:var(--white);font-family:"Dosis",sans-serif;font-weight:500;font-size:16px;letter-spacing:1px;display:flex;align-items:center;justify-content:center}

/* Inside spread */
.resources{background:var(--paper);color:var(--ink)}
.faq{background:var(--green);color:var(--white)}
.resources .heading,.faq .heading{left:0;right:0;top:348px;text-align:center;font-size:31px}
.resources .heading{color:var(--plum)}
.qa{left:36px;right:36px;top:414px;font-size:10.6px;line-height:13.4px;text-align:justify}
.qa h3{font-size:10.6px;font-weight:700;text-transform:uppercase;margin-top:14px}
.qa h3:first-child{margin-top:0}
.faq .qa p{color:#eef3e4}
.url-foot{left:0;right:0;bottom:18px;text-align:center;font-family:"Dosis",sans-serif;font-weight:500;font-size:15px;letter-spacing:1px;color:var(--white)}

.services{background:linear-gradient(160deg,var(--plum) 0%,var(--plum-deep) 100%);color:var(--white)}
.services .heading{left:0;right:0;top:34px;text-align:center;color:var(--lime);font-size:32px}
.rule{left:150px;width:62px;top:86px;height:3px;background:var(--white)}
.services-copy{left:32px;right:32px;top:112px;font-size:10.6px;line-height:13.6px;text-align:justify}
.services-copy strong{display:block;margin-top:14px;font-weight:700}
.service{left:32px;width:210px;font-size:10.8px;line-height:13.8px}
.service h4{color:var(--lime);font-size:10.8px;font-weight:700;text-transform:uppercase}
.service-icon{left:250px;width:80px;height:80px;border-radius:50%;border:2px solid var(--white);display:flex;align-items:center;justify-content:center}
</style>
</head>
<body>

<!-- Outside spread -->
<section class="spread spread--outside">
  <article class="panel about">
    <svg class="abs" style="left:0;top:0" width="363" height="130" viewBox="0 0 363 130" aria-hidden="true">
      <path d="M0 0H363V78C300 50 200 70 140 98C90 120 40 116 0 104Z" fill="var(--green)"/>
      <path d="M363 78C300 50 200 70 140 98C220 72 300 68 363 92Z" fill="var(--white)"/>
    </svg>
    <h2 class="heading abs">About Us</h2>
    <div class="portrait placeholder" style="left:46px;top:120px" role="img" aria-label="Portrait of the owner"></div>
    <div class="portrait placeholder" style="left:190px;top:120px" role="img" aria-label="Portrait of the staffing coordinator"></div>
    <div class="person abs" style="left:34px;top:264px"><b>Dana Whitlock</b>Owner</div>
    <div class="person abs" style="left:178px;top:264px"><b>Renee Holloway</b>Staffing Coordinator</div>
    <div class="about-copy abs">
      <p>Dana Whitlock is a native of Iowa but has lived in Colorado long enough to call it home. She graduated in 1998 from Westridge Community College with an A.A.S. degree in Interpreter Preparation and has done most of her interpreting work in the educational interpreting field. She is currently enrolled in the ASL-English Interpretation BA program at Northfield State University. Recognizing the great need for qualified interpreters in the public education system, she partnered with Renee Holloway to offer school districts State Department of Education (SDE) credentialed interpreters for Deaf and Hard of Hearing students. By using credentialed interpreters, school districts are able to maintain compliance with SDE rules, as well as securing professional and highly qualified interpreters for their students.</p>
      <p>Renee Holloway is the staffing coordinator of ORVANTA, LLC. She grew up in California and moved to Colorado in 1996. She graduated from Westridge Community College in 2002 earning her A.A.S in Interpreter Preparation. She currently is obtaining her B.S in Speech Language and Hearing Sciences. In her spare time, she enjoys spending time with her family and friends and volunteering at her church.</p>
    </div>
    <div class="placeholder" style="left:0;bottom:0;width:363px;height:212px;background:linear-gradient(135deg,#b99a86,#6e6a78);clip-path:path('M0 60C90 10 230 0 363 40V212H0Z')" role="img" aria-label="Photo of a group practising sign language"></div>
    <svg class="abs" style="left:0;bottom:0" width="363" height="212" viewBox="0 0 363 212" aria-hidden="true">
      <path d="M0 60C90 10 230 0 363 40" fill="none" stroke="var(--green)" stroke-width="7"/>
    </svg>
  </article>

  <article class="panel careers">
    <svg class="abs" style="left:0;top:0" width="363" height="340" viewBox="0 0 363 340" aria-hidden="true">
      <path d="M363 180C330 120 300 70 250 40C300 60 340 100 363 150Z" fill="var(--white)" opacity=".9"/>
      <path d="M0 0H363V40C250 20 150 30 0 20Z" fill="var(--green-dark)" opacity=".5"/>
    </svg>
    <div class="map placeholder" role="img" aria-label="Map of the metro service area"></div>
    <h2 class="heading abs" style="top:324px">Careers</h2>
    <p class="careers-copy abs">Whether you prefer K-12 educational settings or working with adults we have a need for you. If you are passionate about your job and want to work with a company that exudes the highest professional standards, please contact us.</p>
    <h2 class="heading abs" style="top:522px;font-size:27px">Contact Us</h2>
    <p class="contact abs"><b>ORVANTA / TKPR, LLC</b><br>Voice : (720) 555-0148<br>Text : (303) 555-0192<br>Email Us<br>PO BOX 418200<br>Lakeview, Colorado 80415</p>
    <div class="request abs" style="top:716px">
      <svg width="46" height="60" viewBox="0 0 46 60" aria-hidden="true">
        <path d="M8 30V12a4 4 0 0 1 8 0v14V6a4 4 0 0 1 8 0v20V8a4 4 0 0 1 8 0v20V14a4 4 0 0 1 8 0v24c0 12-8 20-18 20S6 50 4 42L2 34a4 4 0 0 1 6-4Z" fill="var(--white)"/>
        <path d="M24 48l-6-6a3.5 3.5 0 0 1 6-4a3.5 3.5 0 0 1 6 4Z" fill="var(--green)"/>
      </svg>
      <span class="request-label">Request an<br>Interpreter</span>
    </div>
  </article>

  <article class="panel cover">
    <div class="cover-top abs"></div>
    <div class="brand abs">
      <span class="brand-mark"></span>
      <span class="brand-name">ORVANTA, LLC</span>
    </div>
    <div class="placeholder" style="left:0;top:150px;width:363px;height:400px;background:linear-gradient(160deg,#e9e4d6,var(--photo-warm) 55%,#bfa8a2);clip-path:path('M0 0H363V355C250 410 100 410 0 370Z')" role="img" aria-label="Photo of two children signing to each other"></div>
    <svg class="abs" style="left:0;top:480px" width="363" height="100" viewBox="0 0 363 100" aria-hidden="true">
      <path d="M0 40C100 80 250 80 363 25" fill="none" stroke="var(--green)" stroke-width="9"/>
    </svg>
    <h1 class="title abs">Clearview<br>&amp; Kindred</h1>
    <p class="subtitle abs">SIGN LANGUAGE INTERPRETERS</p>
    <div class="url-tab abs">www.orvanta-tkpr.com</div>
  </article>
</section>

<!-- Inside spread -->
<section class="spread spread--inside">
  <article class="panel resources">
    <h2 class="heading abs">Resources</h2>
    <div class="qa abs">
      <h3>When do I need to request an interpreter?</h3>
      <p>Sign language interpreters are needed when you communicate with a deaf individual whose primary source of communication is sign language. Always ask the deaf person first if an interpreter is needed. A deaf person who is competent in English when writing, reading and speaking may still want an interpreter for more complex or technical situations to ensure effective communication. Lip reading for some deaf people is taxing and is not a reliable means of understanding a conversation in its entirety.</p>
      <h3>Rights of deaf and hard of hearing/ADA</h3>
      <p>The Americans with Disability Act (ADA) is a law that prohibits discrimination against people with disabilities including deaf and hard of hearing individuals. All businesses and government agencies are required to provide effective communication. Please visit www.access-rights-info.org for more information.</p>
      <h3>Benefits to small businesses</h3>
      <p>Small businesses may qualify for a tax credit under Section 44 of the federal tax code. This incentive was created in 1990 to help small businesses cover ADA related expenses. For more information please visit <u>www.tax-credit-info.org</u></p>
    </div>
  </article>

  <article class="panel faq">
    <h2 class="heading abs">FAQ</h2>
    <div class="qa abs">
      <h3>Can the deaf person bring in their own interpreter?</h3>
      <p>It is not recommended. Professional interpreters are trained and must abide by NRI's professional Code of Conduct. This will ensure message accuracy, impartiality and confidentiality.</p>
      <h3>Is there always a two hour minimum?</h3>
      <p>Many assignments require a two hour minimum however we are more than happy to come up with an agreement that fits your needs.</p>
      <h3>Do you only supply educational interpreters?</h3>
      <p>Although our main focus is educational interpreting, we do provide services for medical and community interpreting as well.</p>
    </div>
    <div class="request abs" style="top:690px">
      <svg width="46" height="60" viewBox="0 0 46 60" aria-hidden="true">
        <path d="M8 30V12a4 4 0 0 1 8 0v14V6a4 4 0 0 1 8 0v20V8a4 4 0 0 1 8 0v20V14a4 4 0 0 1 8 0v24c0 12-8 20-18 20S6 50 4 42L2 34a4 4 0 0 1 6-4Z" fill="var(--white)"/>
        <path d="M24 48l-6-6a3.5 3.5 0 0 1 6-4a3.5 3.5 0 0 1 6 4Z" fill="var(--green)"/>
      </svg>
      <span class="request-label">Request an<br>Interpreter</span>
    </div>
    <p class="url-foot abs">www.orvanta-tkpr.com</p>
  </article>

  <article class="panel services">
    <h2 class="heading abs">Our Services</h2>
    <div class="rule abs"></div>
    <div class="services-copy abs">
      Clearview &amp; Kindred Sign Language Interpreters is the Lakeview Metro area's premier interpreting agency. We have been providing qualified professional Sign Language Interpreting services since 2008. Our interpreters are carefully screened and handpicked to ensure that your communication needs are met with ease and comfort. We offer superior service at competitive prices with excellent customer service.
      <strong>Although we specialize in Medical and Educational Interpreting, we also provide services for:</strong>
    </div>
    <div class="service abs" style="top:304px"><h4>Educational</h4>K-12 Settings<br>Post-Secondary<br>Parent/Teacher Conference<br>IEP Meetings<br>Staff Meetings<br>Extracurricular Activities</div>
    <div class="service-icon abs" style="top:306px"><svg width="40" height="40" viewBox="0 0 40 40" fill="none" stroke="#fff" stroke-width="2" aria-hidden="true"><path d="M4 10h13a3 3 0 0 1 3 3v20a3 3 0 0 0-3-3H4Z"/><path d="M36 10H23a3 3 0 0 0-3 3v20a3 3 0 0 1 3-3h13Z"/></svg></div>

    <div class="service abs" style="top:419px"><h4>Business</h4>Staff Meetings<br>Interviews &amp; Orientations<br>Conferences<br>Job Training</div>
    <div class="service-icon abs" style="top:410px"><svg width="40" height="40" viewBox="0 0 40 40" fill="none" stroke="#fff" stroke-width="2" aria-hidden="true"><path d="M6 34h28"/><rect x="9" y="22" width="5" height="12"/><rect x="18" y="16" width="5" height="18"/><rect x="27" y="10" width="5" height="24"/><path d="M8 16l9-7 7 4 9-8"/></svg></div>

    <div class="service abs" style="top:511px"><h4>Special Occasions</h4>Weddings<br>Funerals<br>Graduations</div>
    <div class="service-icon abs" style="top:502px"><svg width="40" height="40" viewBox="0 0 40 40" fill="none" stroke="#fff" stroke-width="2" aria-hidden="true"><path d="M20 6c-7 0-10 6-10 12v8l-4 4h28l-4-4v-8c0-6-3-12-10-12Z"/><path d="M16 34a4 4 0 0 0 8 0"/></svg></div>

    <div class="service abs" style="top:588px"><h4>Medical</h4>Doctor's Appointments<br>ER Visits<br>Patient Education and Counseling<br>Pre-Op/Post-Op Appointments<br>Physical, Speech &amp;<br>Occupational Therapy</div>
    <div class="service-icon abs" style="top:594px"><svg width="40" height="40" viewBox="0 0 40 40" fill="none" stroke="#fff" stroke-width="2" aria-hidden="true"><path d="M20 34S5 25 5 15a7 7 0 0 1 15-3 7 7 0 0 1 15 3c0 10-15 19-15 19Z"/><path d="M10 19h6l3-5 3 9 2-4h6"/></svg></div>

    <div class="service abs" style="top:703px"><h4>Religious</h4>Church Services &amp; Sermons<br>Counseling<br>Religious Ceremonies</div>
    <div class="service-icon abs" style="top:692px"><svg width="40" height="40" viewBox="0 0 40 40" fill="none" stroke="#fff" stroke-width="2" aria-hidden="true"><circle cx="20" cy="16" r="6"/><path d="M20 4v3M9 8l2 2M31 8l-2 2M6 17h3M31 17h3M14 36V28a6 6 0 0 1 12 0v8"/></svg></div>

    <p class="url-foot abs">www.orvanta-tkpr.com</p>
  </article>

  <div class="placeholder" style="left:0;top:0;width:726px;height:320px;background:linear-gradient(135deg,#3f5a2e,var(--photo-green) 50%,#8a9a6c);clip-path:path('M0 0H726V250C500 270 250 290 0 320Z')" role="img" aria-label="Close-up photo of hands signing in front of pine branches"></div>
  <svg class="abs" style="left:0;top:230px" width="726" height="100" viewBox="0 0 726 100" aria-hidden="true">
    <path d="M0 90C250 60 500 40 726 20" fill="none" stroke="var(--white)" stroke-width="8"/>
  </svg>
</section>

</body>
</html>
```